Step and Repeat Backdrop for wedding reception photo booth

Would like to have a Step and Repeat Backdrop (8 foot high by 10 foot wide) that incorporates the wedding logo (attached) and the names Elena and Gavin. Background should be white, and wedding colors are burgundy and gold. Show me creativity :-) I have included some random samples.

```html
<!DOCTYPE html>
<html lang="en">
<head>
<meta charset="utf-8">
<title>Elena &amp; Gavin – Step and Repeat Backdrop</title>
<link rel="stylesheet" href="https://fonts.googleapis.com/css2?family=Cormorant+Garamond:wght@600&family=Great+Vibes&display=swap">
<style>
  :root {
    --paper: #ffffff;
    --gold-deep: #7f6e2e;
    --gold-bright: #cba326;
    --gold-monogram: #ad8c52;
    --gold-script: #a8892c;
    --ornament-soft: #e6d6ad;
    --ornament-mid: #c9ac6e;
  }
  * { margin: 0; padding: 0; box-sizing: border-box; }
  html, body {
    width: 1200px;
    height: 1200px;
    overflow: hidden;
    background: var(--paper);
  }
  .backdrop {
    position: relative;
    width: 1200px;
    height: 1200px;
    background: var(--paper);
  }
  .backdrop-frame {
    position: absolute;
    left: 128px;
    top: 130px;
    width: 944px;
    height: 940px;
    border: 11px solid;
    border-image: linear-gradient(90deg, var(--gold-deep), var(--gold-bright)) 1;
  }
  .monogram {
    position: absolute;
    width: 140px;
    height: 70px;
    margin-left: -70px;
    margin-top: -35px;
    display: flex;
    align-items: center;
    justify-content: center;
    font-family: "Cormorant Garamond", serif;
    font-weight: 600;
    font-size: 60px;
    line-height: 1;
    color: var(--gold-monogram);
    letter-spacing: -2px;
  }
  .name-tile {
    position: absolute;
    width: 98px;
    height: 98px;
    border: 2.5px solid;
    border-image: linear-gradient(90deg, var(--gold-deep), var(--gold-bright)) 1;
    background: var(--paper);
  }
  .name-tile .ornament {
    position: absolute;
    left: 50%;
    width: 68px;
    height: 18px;
    margin-left: -34px;
    border-radius: 9px;
    background: linear-gradient(90deg, var(--ornament-soft), var(--ornament-mid) 50%, var(--ornament-soft));
    opacity: 0.55;
  }
  .name-tile .ornament-top { top: 6px; }
  .name-tile .ornament-bottom { bottom: 6px; }
  .name-tile .couple-names {
    position: absolute;
    left: 0;
    right: 0;
    top: 29px;
    text-align: center;
    font-family: "Great Vibes", cursive;
    font-size: 19px;
    line-height: 16px;
    color: var(--gold-script);
  }
</style>
</head>
<body>
<main class="backdrop">
  <div class="backdrop-frame"></div>

  <!-- Monogram row 1 -->
  <div class="monogram" style="left:245px; top:250px;">E&amp;G</div>
  <div class="monogram" style="left:483px; top:250px;">E&amp;G</div>
  <div class="monogram" style="left:721px; top:250px;">E&amp;G</div>
  <div class="monogram" style="left:966px; top:250px;">E&amp;G</div>

  <!-- Monogram row 2 -->
  <div class="monogram" style="left:245px; top:478px;">E&amp;G</div>
  <div class="monogram" style="left:483px; top:478px;">E&amp;G</div>
  <div class="monogram" style="left:721px; top:478px;">E&amp;G</div>
  <div class="monogram" style="left:966px; top:478px;">E&amp;G</div>

  <!-- Monogram row 3 -->
  <div class="monogram" style="left:245px; top:703px;">E&amp;G</div>
  <div class="monogram" style="left:483px; top:703px;">E&amp;G</div>
  <div class="monogram" style="left:721px; top:703px;">E&amp;G</div>
  <div class="monogram" style="left:966px; top:703px;">E&amp;G</div>

  <!-- Monogram row 4 -->
  <div class="monogram" style="left:245px; top:945px;">E&amp;G</div>
  <div class="monogram" style="left:483px; top:945px;">E&amp;G</div>
  <div class="monogram" style="left:721px; top:945px;">E&amp;G</div>
  <div class="monogram" style="left:966px; top:945px;">E&amp;G</div>

  <!-- Name tiles row 1 -->
  <div class="name-tile" style="left:313px; top:314px;">
    <div class="ornament ornament-top" role="img" aria-label="Gold filigree flourish"></div>
    <p class="couple-names">Elena &amp;<br>Gavin</p>
    <div class="ornament ornament-bottom" role="img" aria-label="Gold filigree flourish"></div>
  </div>
  <div class="name-tile" style="left:549px; top:314px;">
    <div class="ornament ornament-top" role="img" aria-label="Gold filigree flourish"></div>
    <p class="couple-names">Elena &amp;<br>Gavin</p>
    <div class="ornament ornament-bottom" role="img" aria-label="Gold filigree flourish"></div>
  </div>
  <div class="name-tile" style="left:793px; top:314px;">
    <div class="ornament ornament-top" role="img" aria-label="Gold filigree flourish"></div>
    <p class="couple-names">Elena &amp;<br>Gavin</p>
    <div class="ornament ornament-bottom" role="img" aria-label="Gold filigree flourish"></div>
  </div>

  <!-- Name tiles row 2 -->
  <div class="name-tile" style="left:313px; top:533px;">
    <div class="ornament ornament-top" role="img" aria-label="Gold filigree flourish"></div>
    <p class="couple-names">Elena &amp;<br>Gavin</p>
    <div class="ornament ornament-bottom" role="img" aria-label="Gold filigree flourish"></div>
  </div>
  <div class="name-tile" style="left:549px; top:533px;">
    <div class="ornament ornament-top" role="img" aria-label="Gold filigree flourish"></div>
    <p class="couple-names">Elena &amp;<br>Gavin</p>
    <div class="ornament ornament-bottom" role="img" aria-label="Gold filigree flourish"></div>
  </div>
  <div class="name-tile" style="left:793px; top:533px;">
    <div class="ornament ornament-top" role="img" aria-label="Gold filigree flourish"></div>
    <p class="couple-names">Elena &amp;<br>Gavin</p>
    <div class="ornament ornament-bottom" role="img" aria-label="Gold filigree flourish"></div>
  </div>

  <!-- Name tiles row 3 -->
  <div class="name-tile" style="left:313px; top:776px;">
    <div class="ornament ornament-top" role="img" aria-label="Gold filigree flourish"></div>
    <p class="couple-names">Elena &amp;<br>Gavin</p>
    <div class="ornament ornament-bottom" role="img" aria-label="Gold filigree flourish"></div>
  </div>
  <div class="name-tile" style="left:549px; top:776px;">
    <div class="ornament ornament-top" role="img" aria-label="Gold filigree flourish"></div>
    <p class="couple-names">Elena &amp;<br>Gavin</p>
    <div class="ornament ornament-bottom" role="img" aria-label="Gold filigree flourish"></div>
  </div>
  <div class="name-tile" style="left:793px; top:776px;">
    <div class="ornament ornament-top" role="img" aria-label="Gold filigree flourish"></div>
    <p class="couple-names">Elena &amp;<br>Gavin</p>
    <div class="ornament ornament-bottom" role="img" aria-label="Gold filigree flourish"></div>
  </div>
</main>
</body>
</html>
```